PowerPoint Presentation

We are looking for a new PPT layout template existing of a cover page, three internal pages - one with text bullets, one with a picture/information and one with more of a table for pricing information and the last a last "thank you - contact info" page. Feel free to grab any graphics from our website at www.brightharbor.com

Any product can be chosen from our products page. Colors are cyan and orange and feel free to choose darker backgrounds for the front and end page. Also included in the graphics is our new business card design.

Also note we are updating our website, and have attached a sample of how it looks for reference.

Reason: We are still looking for submissions for our PowerPoint presentation. We have increased the award amount as well.

Target Market(s)

Target market is private industry professionals, public safety organizations, and state and local government agencies.

Industry/Entity Type

Business

Colors
33a6d7
86cae6
cee9f5
f68d4d
f8ba93
fce2d4

```html
<!DOCTYPE html>
<html lang="en">
<head>
<meta charset="utf-8">
<title>Project Title Here</title>
<link rel="stylesheet" href="https://fonts.googleapis.com/css2?family=Open+Sans:wght@400;600&family=Roboto+Condensed:wght@700&display=swap">
<style>
  :root {
    --cyan: #00aaec;
    --orange: #ff8200;
    --rule-grey: #5f6062;
    --ring-grey: #d4d6d8;
    --logo-grey: #6d6e71;
    --ink: #111111;
    --paper: #ffffff;
  }
  html, body {
    margin: 0;
    padding: 0;
    overflow: hidden;
    background: var(--paper);
  }
  .slide {
    position: relative;
    width: 1200px;
    height: 900px;
    overflow: hidden;
    background: var(--paper);
  }
  .header-wave {
    position: absolute;
    top: 0;
    left: 0;
    width: 1200px;
    height: 260px;
  }
  .header-wave .fill { fill: var(--cyan); }
  .header-wave .rule { fill: none; stroke: var(--rule-grey); stroke-width: 5; }
  .slide-title {
    position: absolute;
    top: 25px;
    left: 22px;
    margin: 0;
    font-family: "Roboto Condensed", "Arial Narrow", sans-serif;
    font-weight: 700;
    font-size: 58px;
    line-height: 1;
    letter-spacing: 3px;
    color: var(--paper);
  }
  .bullet-list {
    list-style: none;
    margin: 0;
    padding: 0;
  }
  .bullet-item {
    position: absolute;
    left: 22px;
    display: flex;
    align-items: center;
    height: 50px;
    margin-top: -25px;
    font-family: "Open Sans", Arial, sans-serif;
    font-size: 25.8px;
    color: var(--ink);
    white-space: nowrap;
  }
  .bullet-icon {
    width: 40px;
    height: 40px;
    margin-right: 25px;
    flex: none;
  }
  .footer-band {
    position: absolute;
    left: 0;
    bottom: 0;
    width: 1200px;
    height: 28px;
    background: var(--orange);
  }
  .brand-name {
    position: absolute;
    right: 8px;
    bottom: 30px;
    margin: 0;
    font-family: "Open Sans", Arial, sans-serif;
    font-weight: 600;
    font-size: 34px;
    letter-spacing: 1px;
    color: var(--logo-grey);
  }
</style>
</head>
<body>
<div class="slide">
  <svg class="header-wave" viewBox="0 0 1200 260" aria-hidden="true">
    <path class="fill" d="M0,0 H1200 V240 C1100,180 900,110 600,105 L0,102 Z"/>
    <path class="rule" d="M0,102 L600,105 C900,110 1100,180 1200,240"/>
  </svg>
  <h1 class="slide-title">PROJECT TILE HERE</h1>

  <ul class="bullet-list">
    <li class="bullet-item" style="top:194px"><svg class="bullet-icon" viewBox="0 0 40 40" aria-hidden="true"><circle cx="20" cy="20" r="17" fill="none" stroke="#d4d6d8" stroke-width="3"/><polyline points="16,11 25,20 16,29" fill="none" stroke="#00aaec" stroke-width="5"/></svg>Lorem ipsum dolor sit ipsum Lorem ipsum dolor sit ipsum Lorem ipsum</li>
    <li class="bullet-item" style="top:285px"><svg class="bullet-icon" viewBox="0 0 40 40" aria-hidden="true"><circle cx="20" cy="20" r="17" fill="none" stroke="#d4d6d8" stroke-width="3"/><polyline points="16,11 25,20 16,29" fill="none" stroke="#00aaec" stroke-width="5"/></svg>Lorem ipsum dolor sit ipsum Lorem ipsum dolor sit ipsum Lorem ipsum</li>
    <li class="bullet-item" style="top:366px"><svg class="bullet-icon" viewBox="0 0 40 40" aria-hidden="true"><circle cx="20" cy="20" r="17" fill="none" stroke="#d4d6d8" stroke-width="3"/><polyline points="16,11 25,20 16,29" fill="none" stroke="#00aaec" stroke-width="5"/></svg>Lorem ipsum dolor sit ipsum Lorem ipsum dolor sit ipsum Lorem ipsum</li>
    <li class="bullet-item" style="top:455px"><svg class="bullet-icon" viewBox="0 0 40 40" aria-hidden="true"><circle cx="20" cy="20" r="17" fill="none" stroke="#d4d6d8" stroke-width="3"/><polyline points="16,11 25,20 16,29" fill="none" stroke="#00aaec" stroke-width="5"/></svg>Lorem ipsum dolor sit ipsum Lorem ipsum dolor sit ipsum Lorem ipsum</li>
    <li class="bullet-item" style="top:551px"><svg class="bullet-icon" viewBox="0 0 40 40" aria-hidden="true"><circle cx="20" cy="20" r="17" fill="none" stroke="#d4d6d8" stroke-width="3"/><polyline points="16,11 25,20 16,29" fill="none" stroke="#00aaec" stroke-width="5"/></svg>Lorem ipsum dolor sit ipsum Lorem ipsum dolor sit ipsum Lorem ipsum</li>
    <li class="bullet-item" style="top:660px"><svg class="bullet-icon" viewBox="0 0 40 40" aria-hidden="true"><circle cx="20" cy="20" r="17" fill="none" stroke="#d4d6d8" stroke-width="3"/><polyline points="16,11 25,20 16,29" fill="none" stroke="#00aaec" stroke-width="5"/></svg>Lorem ipsum dolor sit ipsum Lorem ipsum dolor sit ipsum Lorem ipsum</li>
  </ul>

  <p class="brand-name">BRIGHTHARBOR</p>
  <div class="footer-band"></div>
</div>
</body>
</html>
```